Hi Tech startup needs an investor presentation

We need an investor presentaiton for a new company based in Russia. We develop innovative solutions connecting customers and businesses via VoIP. Our initial product is an iPhone / Android app connecting customers directly to call centers / help desks bypassing calling (800) numbers. This also saves money for companies who do not need to pay for (800) lines.
Updates

Hi guys!

I have now made the contest committed, so please participate.

Industry/Entity Type

It Company

Requirements
Must have
• The ppt must follow the structure already suggested in the uploaded ppt
Nice to have
• Some nice graphic solutions, pictograms and so on instead of large chunks of text
Should not have
• Should not use old-style fonts and solutions.
• Also, not too cocky please.

```html
<!DOCTYPE html>
<html lang="en">
<head>
<meta charset="utf-8">
<title>Callvista — investor presentation</title>
<link href="https://fonts.googleapis.com/css2?family=Ubuntu:wght@300;400;500;700&display=swap" rel="stylesheet">
<style>
:root{
  --ink:#3a2806;
  --text:#2b2b2b;
  --accent:#f08a12;
  --sun:#f9c21e;
  --sun-light:#fbd54a;
  --sun-deep:#eea514;
  --brand-grey:#4a4a4a;
  --dark:#2a2420;
  --page:#000;
}
*{box-sizing:border-box;margin:0;padding:0}
html,body{width:1178px;height:1200px;overflow:hidden;background:var(--page)}
body{position:relative;font-family:"Ubuntu",sans-serif;color:var(--text)}
.slide{position:absolute;width:377px;height:283px;background:#fff;overflow:hidden}
.c1{left:10px}.c2{left:398px}.c3{left:788px}
.r1{top:10px}.r2{top:307px}.r3{top:606px}.r4{top:903px}
.head{position:absolute;left:0;top:0;width:100%;height:32px;background:linear-gradient(90deg,var(--sun-deep),var(--sun) 55%,var(--sun-light));display:flex;align-items:center;padding:0 10px;border-bottom:1px solid #d98d0c}
.head h2{font-size:12.5px;font-weight:500;color:var(--ink);line-height:1.1}
.head h2.small{font-size:8.6px;font-weight:500}
.foot{position:absolute;left:0;bottom:0;width:100%;height:62px}
.brand{position:absolute;left:8px;bottom:6px;display:flex;align-items:center;gap:3px;font-weight:300;font-size:18px;color:var(--brand-grey);letter-spacing:-.3px}
.brand .dot{width:19px;height:19px;border-radius:50%;background:var(--sun);border:2px solid #fff;box-shadow:0 0 0 1px #c98a0a}
.copy{position:absolute;right:36px;bottom:9px;font-size:6px;color:#3a2806}
.pg{position:absolute;right:9px;bottom:5px;width:19px;height:19px;border-radius:50%;background:var(--dark);color:#fff;font-size:7px;font-weight:700;display:flex;align-items:center;justify-content:center}
.bullets{position:absolute;left:10px;right:12px;list-style:none}
.bullets li{position:relative;padding-left:18px;font-size:6.8px;line-height:1.5}
.bullets li::before{content:"›";position:absolute;left:0;top:0;width:10px;height:10px;border-radius:50%;background:var(--sun);color:var(--ink);font-size:9px;font-weight:700;line-height:9px;text-align:center}
.hl{color:var(--accent)}
.label{position:absolute;font-size:9px;color:var(--accent)}
.cover{background:#fff}
.cover .sky{position:absolute;inset:0}
.cover h1{position:absolute;left:26px;top:50px;font-size:19px;font-weight:700;color:var(--ink)}
.cover p{position:absolute;left:26px;top:78px;font-size:9.3px;line-height:1.55;color:var(--ink);width:220px}
.cover .brand{left:auto;right:12px;bottom:22px;font-size:30px;gap:6px}
.cover .brand .dot{width:36px;height:36px}
.step{position:absolute;left:22px;right:20px;height:54px;border:1px solid #ddd;border-radius:3px;background:linear-gradient(#fff,#f6f6f6);box-shadow:0 1px 2px rgba(0,0,0,.15)}
.num{position:absolute;width:17px;height:17px;border-radius:50%;background:var(--sun);border:1px solid #c88a0a;font-size:9px;font-weight:700;color:var(--ink);display:flex;align-items:center;justify-content:center}
.step h3{font-size:6.6px;font-weight:500}
.step ul{list-style:none;font-size:5.2px;line-height:1.45;margin-top:2px}
.step ul li::before{content:"› ";font-weight:700}
.art{position:absolute;border-radius:3px}
.team-intro{position:absolute;left:10px;top:42px;right:14px;font-size:6.4px;line-height:1.5}
.member{position:absolute;top:66px;width:170px;text-align:center}
.member .photo{width:64px;height:64px;border-radius:50%;margin:0 auto 5px;background:radial-gradient(circle at 50% 40%,#b9bcc2,#6d7078)}
.member .name{font-size:8.6px;color:var(--accent)}
.member .role{font-size:6.6px;font-weight:500;margin:1px 0 3px}
.member .bio{font-size:5.3px;line-height:1.5}
.team-note{position:absolute;left:0;right:0;text-align:center;font-size:6.4px}
.co{position:absolute;font-weight:700;font-size:11px;color:#444}
.contact-top{position:absolute;left:0;top:0;width:100%;height:117px;background:linear-gradient(120deg,var(--sun-deep),var(--sun) 60%,var(--sun-light))}
.contact-top h2{position:absolute;top:64px;width:100%;text-align:center;font-size:13px;font-weight:500;line-height:1.45;color:var(--ink)}
.contact .who{position:absolute;top:133px;width:100%;text-align:center}
.contact .who .name{font-size:11px;color:var(--accent)}
.contact .who .role{font-size:9px}
.contact ul{position:absolute;left:134px;top:177px;list-style:none;font-size:6.6px}
.contact li{display:flex;align-items:center;gap:5px;margin-bottom:8px}
.ic{width:11px;height:11px;border-radius:50%;background:var(--sun);display:flex;align-items:center;justify-content:center}
.chart-label{position:absolute;font-size:6.2px;line-height:1.25;text-align:center}
</style>
</head>
<body>

<svg width="0" height="0" style="position:absolute">
  <defs>
    <linearGradient id="sunfill" x1="0" y1="0" x2="1" y2="0">
      <stop offset="0" stop-color="#f5b417"/>
      <stop offset="1" stop-color="#f9c724"/>
    </linearGradient>
    <symbol id="swoosh" viewBox="0 0 377 62" preserveAspectRatio="none">
      <path d="M0 42 C110 47 250 40 377 19 L377 62 L0 62 Z" fill="url(#sunfill)"/>
      <path d="M0 42 C110 47 250 40 377 19" fill="none" stroke="#e08a0c" stroke-width="1.2"/>
      <path d="M0 39 C120 44 250 36 377 15" fill="none" stroke="#fbd76a" stroke-width=".8"/>
    </symbol>
  </defs>
</svg>

<!-- 1 Title -->
<section class="slide cover c1 r1">
  <svg class="sky" viewBox="0 0 377 283" preserveAspectRatio="none">
    <defs><linearGradient id="coverfill" x1="0" y1="0" x2="1" y2="1"><stop offset="0" stop-color="#f7b51a"/><stop offset="1" stop-color="#fbcf3a"/></linearGradient></defs>
    <path d="M0 0 H377 V150 C260 178 120 205 0 205 Z" fill="url(#coverfill)"/>
    <path d="M20 182 C150 172 250 188 310 192" fill="none" stroke="#fff" stroke-width="1.2" opacity=".8"/>
    <path d="M0 205 C120 205 260 178 377 150" fill="none" stroke="#e08a0c" stroke-width="1.4"/>
  </svg>
  <h1>PROJECT TITLE HERE</h1>
  <p>Lorem ipsum dolor sit&nbsp; Lorem ipsum dolor sit Lorem ipsum dolor sit&nbsp; Lorem ipsum dolor sit Lorem ipsum dolor sit</p>
  <div class="brand"><span class="dot"></span>callvista</div>
</section>

<!-- 2 Who we are -->
<section class="slide c2 r1">
  <header class="head"><h2>Who we are and what we believe</h2></header>
  <ul class="bullets" style="top:55px">
    <li style="margin-bottom:17px">St.-Petersburg-based developer and marketer of proprietary cloud-based VoIP solutions;</li>
    <li style="margin-bottom:15px">We directly address the need for effective, efficient, cheap and easy communication between businesses and customers;</li>
    <li style="margin-bottom:15px">We do not like the way corporation treat their customers, we are not happy with the way large telecom operators work, and we are not happy about corporate digital footprint and information, which is available to customers;</li>
    <li>We strongly believe that information has to be free and readily available to anyone with data connection and that communication has to be absolutely free and unchained.</li>
  </ul>
  <svg class="foot"><use href="#swoosh"/></svg>
  <div class="brand"><span class="dot"></span>callvista</div><div class="copy">Copyright text here</div><div class="pg">01</div>
</section>

<!-- 3 Problem -->
<section class="slide c3 r1">
  <header class="head"><h2 class="small">Problem: both customers and businesses have significant problems<br>with “toll free” (800) numbers</h2></header>
  <div class="label" style="left:28px;top:40px">Customers:</div>
  <ul class="bullets" style="top:58px">
    <li style="margin-bottom:9px">Long waiting minutes – poor customer experience;</li>
    <li>Convoluted navigation, poor interactive voice response (IVR) – you always end up at the wrong desk and speak to the wrong person – even poorer customer experience.</li>
  </ul>
  <div class="label" style="left:28px;top:117px">Businesses:</div>
  <ul class="bullets" style="top:136px">
    <li style="margin-bottom:15px">“Toll free” numbers are only free for the customers, as businesses in the United States pay up to $0.06 per minute on (800) numbers;</li>
    <li style="margin-bottom:15px">10 customers are lost per each complaining client in the United States (Bizpulse study);</li>
    <li>Poor IVR only makes it worse, as bills stack up and customers are dissatisfied.</li>
  </ul>
  <svg class="foot"><use href="#swoosh"/></svg>
  <div class="brand"><span class="dot"></span>callvista</div><div class="copy">Copyright text here</div><div class="pg">01</div>
</section>

<!-- 4 Solution -->
<section class="slide c1 r2">
  <header class="head"><h2>Solution – mobile cloud-based business phonebook</h2></header>
  <ul class="bullets" style="top:42px">
    <li style="margin-bottom:6px;font-size:6.2px"><span class="hl">Find information about businesses –</span> simple column-browser-style menu allowing you to browse industries / companies / departments / typical problems and then connect to the right person right away;</li>
    <li style="margin-bottom:9px;font-size:6.2px">Navigation is completed <span class="hl">before</span> the call is made;</li>
    <li style="margin-bottom:9px;font-size:6.2px">Shorter calls, <span class="hl">better customer experience;</span></li>
    <li style="margin-bottom:9px;font-size:6.2px">Shorter calls, <span class="hl">less phone bills</span> for the business;</li>
    <li style="margin-bottom:9px;font-size:6.2px">We operate telephony through our <span class="hl">own proprietary phone solution</span> based on Callvista IP-PBX;</li>
    <li style="margin-bottom:9px;font-size:6.2px">VoIP means our minutes are actually <span class="hl">FREE</span> rather than traditional “toll free” minutes in exchange for as low as <span class="hl">$1 a month</span> per user (<span class="hl">25x-50x economy</span> depending on your price plan);</li>
    <li style="margin-bottom:9px;font-size:6.2px"><span class="hl">Better customer experience</span> means <span class="hl">more sales</span>, and more <span class="hl">loyal customers;</span></li>
    <li style="font-size:6.2px"><span class="hl">Additional services</span> like calls from web / social networks / etc</li>
  </ul>
  <svg class="foot"><use href="#swoosh"/></svg>
  <div class="brand"><span class="dot"></span>callvista</div><div class="copy">Copyright text here</div><div class="pg">01</div>
</section>

<!-- 5 Steps -->
<section class="slide c2 r2">
  <header class="head"><h2>Slide title here</h2></header>
  <div class="step" style="top:40px">
    <div class="art" role="img" aria-label="Laptop and phone showing the app" style="left:14px;top:6px;width:80px;height:42px;background:linear-gradient(#d9dde3,#8e959f)"></div>
    <div style="position:absolute;left:108px;top:5px;right:6px">
      <h3>Easy installation and set up process</h3>
      <ul><li>Quick and easy;</li><li>Free;</li><li>No need to use your phone memory, the directory is fetched from the cloud on each call</li></ul>
    </div>
  </div>
  <div class="num" style="left:14px;top:63px">1</div>
  <div class="step" style="top:112px">
    <div style="position:absolute;left:6px;top:4px;width:160px">
      <h3>All the information you need is in your phone!</h3>
      <ul><li>Local-review content;</li><li>Easy navigation between companies / departments;</li><li>Problem evaluation forms to direct you to the right desk;</li><li>One-click connection</li></ul>
    </div>
    <div class="art" role="img" aria-label="Caller and agent linked through a cloud" style="left:168px;top:5px;width:150px;height:44px;background:linear-gradient(90deg,#cfd3d8,#9fc4e6 50%,#cfd3d8)"></div>
  </div>
  <div class="num" style="left:343px;top:132px">2</div>
  <div class="step" style="top:182px">
    <div class="art" role="img" aria-label="Person jumping out of a tablet screen" style="left:28px;top:5px;width:80px;height:44px;background:linear-gradient(#e6ecf2,#a9b3bf)"></div>
    <div style="position:absolute;left:132px;top:21px;font-size:7px;color:var(--ink)">Start enjoying the time and money you have saved!</div>
  </div>
  <div class="num" style="left:14px;top:194px">3</div>
  <svg class="foot"><use href="#swoosh"/></svg>
  <div class="brand"><span class="dot"></span>callvista</div><div class="copy">Copyright text here</div><div class="pg">01</div>
</section>

<!-- 6 Team -->
<section class="slide c3 r2">
  <header class="head"><h2>Our Team is the Reason why we think we will succeed</h2></header>
  <p class="team-intro">Core Team presents a healthy mix of tech and business expertise and experience of life and mentality both in Russia and abroad:</p>
  <div class="member" style="left:8px">
    <div class="photo" role="img" aria-label="Portrait of the CEO"></div>
    <div class="name">Arkady Belov (CEO)</div>
    <div class="role">Co-Founder</div>
    <div class="bio">seasoned internet business leader (Nahodka.ru MD) and strategist (ex-Cargo First Head of Development and Neovia Strategies Managing Partner), Northfield School of Economics graduate, Degrees in Law and Financial Management;</div>
  </div>
  <div style="position:absolute;left:188px;top:72px;width:1px;height:120px;background:#ddd"></div>
  <div class="member" style="left:200px">
    <div class="photo" role="img" aria-label="Portrait of the co-founder"></div>
    <div class="name">Oleg Maren</div>
    <div class="role">Co-Founder</div>
    <div class="bio">experienced telecom and IT entrepreneur with multiple projects in Telecom, IT, and Cleantech with a Degree in Secured communication channels;</div>
  </div>
  <p class="team-note" style="top:212px">Our engineers come from Ringhub, Orbita and other leading VoIP and data companies;</p>
  <p class="team-note" style="top:224px">Our advisors come from the ranks of Ringhub, Rosnet and Mobiline</p>
  <svg class="foot"><use href="#swoosh"/></svg>
  <div class="brand"><span class="dot"></span>callvista</div><div class="copy">Copyright text here</div><div class="pg">01</div>
</section>

<!-- 7 Positioning -->
<section class="slide c1 r3">
  <header class="head"><h2 class="small">We do not like clumsy solutions and large companies<br>reaping benefits for no reason</h2></header>
  <svg style="position:absolute;left:0;top:0" width="377" height="283">
    <g stroke="var(--sun-deep)" stroke-width="2.4" fill="none" stroke-linecap="round">
      <line x1="193" y1="62" x2="193" y2="212"/>
      <polyline points="187,70 193,62 199,70"/>
      <line x1="20" y1="151" x2="362" y2="151"/>
      <polyline points="354,145 362,151 354,157"/>
    </g>
  </svg>
  <div class="label" style="left:186px;top:49px;font-size:7px">FREE</div>
  <div class="label" style="left:306px;top:133px;font-size:7px">Usefull Content</div>
  <div class="label" style="left:20px;top:158px;font-size:7px">No content</div>
  <div class="label" style="left:201px;top:206px;font-size:7px">Expensive</div>
  <div class="label" style="left:170px;top:219px;font-size:6.6px;line-height:1.6">Business info<br>Phone solutions</div>
  <div class="brand" style="left:282px;bottom:auto;top:64px;font-size:16px"><span class="dot" style="width:16px;height:16px"></span>callvista</div>
  <div class="co" style="left:92px;top:66px">Chatwave</div>
  <div class="co" style="left:92px;top:91px">Talkloop</div>
  <div class="co" style="left:76px;top:124px">Ringhub</div>
  <div class="co" style="left:36px;top:186px">Telcor</div>
  <div class="co" style="left:124px;top:190px">Veronet</div>
  <div class="co" style="left:304px;top:178px">Localyx</div>
  <svg class="foot"><use href="#swoosh"/></svg>
  <div class="brand"><span class="dot"></span>callvista</div><div class="copy">Copyright text here</div><div class="pg">01</div>
</section>

<!-- 8 Value proposition -->
<section class="slide c2 r3">
  <header class="head"><h2>Value proposition</h2></header>
  <ul class="bullets" style="top:56px">
    <li style="margin-bottom:6px">Joint works in the United States:</li>
  </ul>
  <div style="position:absolute;left:36px;top:76px;font-size:6.8px;line-height:2.2">› Citadel Cloud infrastructure;<br>› FastPipe utilization for easier data transmission</div>
  <ul class="bullets" style="top:123px">
    <li style="margin-bottom:17px">Large market;</li>
    <li style="margin-bottom:14px">Potential for future disruption of the way people behave, make purchases and life choices in addition to getting rid of annoying IVRs and call centers;</li>
    <li>Building a global profitable scalable platform.</li>
  </ul>
  <svg class="foot"><use href="#swoosh"/></svg>
  <div class="brand"><span class="dot"></span>callvista</div><div class="copy">Copyright text here</div><div class="pg">01</div>
</section>

<!-- 9 Contact -->
<section class="slide contact c3 r3">
  <div class="contact-top"><h2>Looking forward to hearing from you<br>and&nbsp; thank you for your time!</h2></div>
  <div class="who"><div class="name">Arkady Belov</div><div class="role">Co-founder</div></div>
  <ul>
    <li><span class="ic"><svg width="7" height="5"><rect x=".5" y=".5" width="6" height="4" fill="none" stroke="#3a2806" stroke-width=".8"/><polyline points=".5,.5 3.5,3 6.5,.5" fill="none" stroke="#3a2806" stroke-width=".8"/></svg></span>a.belov@callvista.example</li>
    <li><span class="ic" style="background:#9fc4e6"><svg width="6" height="6"><circle cx="3" cy="3" r="2.2" fill="none" stroke="#1f4e7a" stroke-width=".9"/></svg></span>arkady.belov</li>
    <li><span class="ic"><svg width="7" height="7"><path d="M1.5 1 L3 1 L3.5 2.5 L2.7 3.2 Q3.5 4.5 4.6 5 L5.3 4.3 L6.5 4.8 L6.4 6.2 Q3.5 6.5 1 3 Z" fill="#3a2806"/></svg></span>+7 900 000 12 34, +7 900 000 56 78</li>
  </ul>
  <svg class="foot"><use href="#swoosh"/></svg>
  <div class="brand"><span class="dot"></span>callvista</div><div class="copy">Copyright text here</div><div class="pg" style="width:13px;height:13px;font-size:5px;bottom:7px">01</div>
</section>

<!-- 10 Pie chart -->
<section class="slide c1 r4">
  <header class="head"><h2>Slide title here</h2></header>
  <svg style="position:absolute;left:98px;top:60px" width="190" height="190" viewBox="0 0 190 190">
    <g transform="rotate(-118 95 95)" fill="none" stroke-width="93">
      <circle cx="95" cy="95" r="46.5" stroke="#b9b9b9" stroke-dasharray="35.06 292.2"/>
      <circle cx="95" cy="95" r="46.5" stroke="#f7d862" stroke-dasharray="64.28 292.2" stroke-dashoffset="-35.06"/>
      <circle cx="95" cy="95" r="46.5" stroke="#f6c62c" stroke-dasharray="40.91 292.2" stroke-dashoffset="-99.34"/>
      <circle cx="95" cy="95" r="46.5" stroke="#e9aa1f" stroke-dasharray="70.13 292.2" stroke-dashoffset="-140.25"/>
      <circle cx="95" cy="95" r="46.5" stroke="#595959" stroke-dasharray="52.6 292.2" stroke-dashoffset="-210.38"/>
      <circle cx="95" cy="95" r="46.5" stroke="#7d7d7d" stroke-dasharray="29.22 292.2" stroke-dashoffset="-262.98"/>
    </g>
    <circle cx="95" cy="95" r="11" fill="#f9c21e" stroke="#fff" stroke-width="2"/>
  </svg>
  <div class="chart-label" style="left:172px;top:81px;color:#fff">Lorem<br>ipsum<br>dolor</div>
  <div class="chart-label" style="left:208px;top:81px">Lorem<br>ipsum<br>dolor</div>
  <div class="chart-label" style="left:236px;top:126px">Lorem ipsum<br>dolor</div>
  <div class="chart-label" style="left:224px;top:187px">Lorem ipsum<br>dolor</div>
  <div class="chart-label" style="left:144px;top:196px">Lorem ipsum dolor<br>Lorem ipsum dolor</div>
  <div class="chart-label" style="left:116px;top:130px;color:#fff">Lorem ipsum dolor<br>Lorem ipsum dolor</div>
  <svg class="foot"><use href="#swoosh"/></svg>
  <div class="brand"><span class="dot"></span>callvista</div><div class="copy">Copyright text here</div><div class="pg">01</div>
</section>

<!-- 11 Bar chart -->
<section class="slide c2 r4">
  <header class="head"><h2>Slide title here</h2></header>
  <svg style="position:absolute;left:0;top:0" width="377" height="283">
    <g font-family="Ubuntu, sans-serif" font-size="6" fill="#2b2b2b">
      <text x="22" y="64">Lorem ipsum text here</text>
      <text x="22" y="89">Lorem ipsum text here</text>
      <text x="22" y="121">Lorem ipsum text here</text>
      <text x="22" y="161">Lorem ipsum text here</text>
      <text x="22" y="207">Lorem ipsum text here</text>
      <text x="92" y="220">Lorem ipsum text here</text>
      <text x="182" y="220">Lorem ipsum text here</text>
      <text x="291" y="220">Lorem ipsum text here</text>
    </g>
    <g>
      <rect x="90" y="155" width="18" height="52" fill="#e0a51c"/>
      <rect x="113" y="116" width="22" height="91" fill="#f0b51f"/>
      <rect x="140" y="132" width="21" height="75" fill="#f0b51f"/>
      <rect x="166" y="161" width="21" height="46" fill="#e0a51c"/>
      <rect x="193" y="193" width="24" height="14" fill="#f0b51f"/>
      <rect x="221" y="201" width="27" height="6" fill="#8a8a8a"/>
      <rect x="251" y="66" width="22" height="141" fill="#e0a51c"/>
      <rect x="276" y="193" width="24" height="14" fill="#f0b51f"/>
      <rect x="303" y="201" width="24" height="6" fill="#f0b51f"/>
      <rect x="330" y="202" width="27" height="5" fill="#8a8a8a"/>
    </g>
  </svg>
  <svg class="foot"><use href="#swoosh"/></svg>
  <div class="brand"><span class="dot"></span>callvista</div><div class="copy">Copyright text here</div><div class="pg">01</div>
</section>

</body>
</html>
```